Stationary and design update for my brand

I need new letterhead, a new business card, business envelope design, new keynote and powerpoint branded slides (16x9). I have logo samples in various styles and brand standards for fonts and colors.

Font styles to use
Sans Serif

```html
<!DOCTYPE html>
<html lang="en">
<head>
<meta charset="utf-8">
<title>Crestway Stationery and Slides</title>
<link rel="stylesheet" href="https://fonts.googleapis.com/css2?family=Cinzel:wght@400&family=Arimo:wght@400;700&display=swap">
<style>
  :root {
    --orange: #ee8a1f;
    --orange-deep: #e27c22;
    --orange-pale: #fbeadb;
    --charcoal: #4a494f;
    --paper: #ffffff;
    --paper-soft: #f7f7f7;
    --ink: #2b2b2b;
    --muted: #8a8a8a;
    --backdrop: #e6e6e8;
    --rule: #d9d9d9;
  }
  * { box-sizing: border-box; margin: 0; padding: 0; }
  html, body { width: 1200px; height: 500px; overflow: hidden; background: var(--backdrop); }
  body { font-family: "Arimo", Arial, sans-serif; color: var(--ink); }
  .canvas { position: relative; width: 1200px; height: 500px; overflow: hidden; }
  .piece { position: absolute; background: var(--paper); box-shadow: 0 2px 6px rgba(0,0,0,.12); overflow: hidden; }

  .wordmark { font-family: "Cinzel", Georgia, serif; font-weight: 400; color: var(--orange); letter-spacing: .02em; line-height: 1; white-space: nowrap; }
  .wordmark.on-orange, .wordmark.on-dark { color: var(--paper); }
  .wordmark.on-dark { color: var(--orange); }
  .tagline { font-size: 2.6px; letter-spacing: .03em; text-transform: uppercase; color: var(--charcoal); white-space: nowrap; margin-top: 1px; }
  .tagline.light { color: var(--paper); }
  .contact { font-size: 4px; line-height: 1.35; color: var(--ink); }
  .contact svg { width: 4px; height: 4px; fill: var(--orange); vertical-align: -0.5px; margin-right: 1px; }
  .faint-band { position: absolute; background: linear-gradient(160deg, rgba(251,234,219,0) 10%, var(--orange-pale) 70%); }

  /* business cards */
  .card { top: 83px; width: 107px; height: 61px; }
  .card-front { left: 119px; background: var(--orange-deep); color: var(--paper); padding: 6px; }
  .card-front .wordmark { font-size: 9px; }
  .card-front .contact { color: var(--paper); font-size: 2.8px; margin-top: 4px; }
  .card-front .contact svg { fill: var(--paper); width: 2.8px; height: 2.8px; }
  .card-front .swoosh { position: absolute; right: 0; bottom: 0; width: 62px; height: 40px; background: linear-gradient(150deg, rgba(255,255,255,0) 35%, #f4f1ee 75%); }
  .card-front .holder { position: absolute; right: 6px; bottom: 5px; text-align: right; }
  .card-front .holder-name { font-family: "Cinzel", Georgia, serif; font-size: 3.4px; color: var(--orange-deep); }
  .card-front .holder-role { font-size: 2.6px; color: var(--charcoal); }
  .card-back { left: 234px; background: var(--paper); }
  .card-back .field { position: absolute; inset: 0; background: linear-gradient(170deg, var(--orange-deep) 40%, #f0a65c 70%, var(--paper) 95%); }
  .card-back .brand { position: absolute; right: 7px; top: 12px; text-align: right; }
  .card-back .wordmark { font-size: 10px; }

  /* envelopes */
  .envelope-front { left: 116px; top: 161px; width: 231px; height: 114px; padding: 16px 9px; }
  .envelope-front .wordmark { font-size: 12px; }
  .envelope-front .contact { margin-top: 6px; }
  .envelope-front .faint-band { right: 0; bottom: 0; width: 190px; height: 90px; }
  .envelope-back { width: 230px; height: 115px; background: var(--paper-soft); }
  .envelope-back .flap { position: absolute; left: 0; top: 0; width: 100%; height: 30px; border-radius: 0 0 8px 8px; display: flex; align-items: center; justify-content: center; }
  .envelope-back .wordmark { font-size: 9px; }
  .envelope-orange { left: 120px; top: 289px; height: 114px; }
  .envelope-orange .flap { background: var(--orange-deep); }
  .envelope-dark { left: 43px; top: 327px; height: 115px; }
  .envelope-dark .flap { background: var(--charcoal); }

  /* letterhead */
  .letterhead { left: 376px; top: 83px; width: 232px; height: 328px; background: #f6f6f6; padding: 14px 12px; }
  .letterhead .wordmark { font-size: 13px; margin-top: 12px; }
  .letterhead .contact { position: absolute; right: 15px; top: 14px; font-size: 3.6px; }
  .letterhead .faint-band { left: 0; right: 0; bottom: 0; height: 80px; }

  /* slides */
  .slide { width: 111px; height: 83px; padding: 6px 7px; }
  .slide-1 { left: 673px; top: 78px; }
  .slide-2 { left: 792px; top: 78px; }
  .slide-3 { left: 673px; top: 168px; }
  .slide-4 { left: 792px; top: 168px; }
  .slide-5 { left: 673px; top: 260px; }
  .slide-6 { left: 792px; top: 260px; }
  .slide.orange { background: var(--orange); color: var(--paper); }
  .slide-head { display: flex; justify-content: flex-end; border-bottom: .5px solid var(--rule); padding-bottom: 1px; }
  .slide-head h3 { font-family: "Cinzel", Georgia, serif; font-weight: 400; font-size: 4px; color: var(--orange); }
  .slide-foot { position: absolute; left: 7px; right: 7px; bottom: 4px; height: 3px; background: var(--orange); font-size: 1.8px; color: var(--paper); padding-left: 2px; line-height: 3px; }
  .slide-body { font-family: Georgia, serif; font-size: 2.2px; line-height: 1.35; color: #555; }
  .slide-body ul { list-style: none; }
  .slide-body li { margin-top: 2px; padding-left: 3px; position: relative; }
  .slide-body li::before { content: ""; position: absolute; left: 0; top: .8px; width: 1.2px; height: 1.2px; background: var(--orange); border-radius: 50%; }
  .cover .wordmark { font-size: 10px; margin-top: 6px; }
  .cover h2 { font-family: "Cinzel", Georgia, serif; font-weight: 400; font-size: 5px; line-height: 1.15; margin-top: 10px; }
  .cover .faint-band { right: 0; bottom: 0; width: 80px; height: 45px; background: linear-gradient(160deg, rgba(255,255,255,0) 20%, rgba(255,255,255,.9) 80%); }
  .photo { background: linear-gradient(135deg, #c9ced3, #8d8f8e 60%, #6b5a4a); }
  .slide-2 .photo { height: 36px; margin-top: 4px; }
  .team { display: flex; justify-content: space-between; margin-top: 3px; }
  .team-member { width: 22px; text-align: left; }
  .team-member .portrait { width: 18px; height: 18px; border-radius: 50%; background: linear-gradient(160deg, #c8c2bb, #6f6860); }
  .team-member .name { font-family: Georgia, serif; font-style: italic; font-size: 2.2px; color: var(--orange); margin-top: 2px; }
  .team-member .bio { font-family: Georgia, serif; font-size: 2px; color: #666; }
  .split { display: flex; gap: 5px; margin-top: 4px; }
  .split .text { flex: 1; }
  .split .lead { font-family: Georgia, serif; font-style: italic; font-size: 2.6px; color: var(--orange); line-height: 1.3; margin-bottom: 3px; }
  .split .photo { width: 47px; height: 50px; background: linear-gradient(180deg, #b9cde0, #4b6a88); }
  .thanks h2 { font-family: "Cinzel", Georgia, serif; font-weight: 400; font-size: 11px; text-align: center; margin-top: 38px; }
  .thanks .faint-band { left: 0; right: 0; top: 8px; height: 30px; background: linear-gradient(180deg, rgba(255,255,255,0), rgba(255,255,255,.18)); }
  .thanks .meta { position: absolute; left: 7px; right: 7px; bottom: 5px; display: flex; justify-content: space-between; font-family: Georgia, serif; font-size: 2.2px; line-height: 1.3; }
  .thanks .meta .right { text-align: right; }

  /* rack cards and pads */
  .rack-orange { left: 932px; top: 80px; width: 59px; height: 111px; background: var(--orange); padding: 6px 5px; }
  .rack-orange .wordmark { font-size: 6.5px; }
  .rack-orange .contact { position: absolute; left: 5px; bottom: 4px; font-size: 2.2px; color: var(--paper); }
  .rack-white { left: 969px; top: 111px; width: 59px; height: 111px; padding: 10px 5px; text-align: center; }
  .rack-white .wordmark { font-size: 8px; }
  .rack-white .base, .pad-white .base { position: absolute; left: 0; right: 0; bottom: 0; background: var(--orange); color: var(--paper); font-family: "Cinzel", Georgia, serif; font-size: 2.6px; text-align: center; }
  .rack-white .base { height: 16px; line-height: 22px; }
  .lined { background-color: var(--paper); background-image: repeating-linear-gradient(180deg, transparent 0 5.6px, var(--rule) 5.6px 6.1px); background-clip: content-box; }
  .note-slim { left: 1036px; top: 82px; width: 58px; height: 109px; padding: 10px 5px 12px; }
  .note-slim .corner, .pad-lined .corner { position: absolute; right: 5px; top: 4px; font-size: 4px; }
  .site { position: absolute; left: 0; right: 0; bottom: 3px; text-align: center; font-size: 2.6px; color: var(--charcoal); }
  .spiral { position: absolute; left: 0; right: 0; top: 0; height: 3px; background: repeating-linear-gradient(90deg, #3c3c3c 0 .6px, transparent .6px 1.6px); }
  .pad-orange { left: 917px; top: 232px; width: 100px; height: 130px; background: var(--orange); padding: 10px 0 0 26px; }
  .pad-orange .wordmark { font-size: 11px; }
  .pad-white { left: 941px; top: 271px; width: 100px; height: 130px; text-align: center; padding-top: 14px; }
  .pad-white .wordmark { font-size: 11px; }
  .pad-white .base { height: 28px; line-height: 44px; font-size: 5px; }
  .pad-lined { left: 1051px; top: 271px; width: 100px; height: 130px; padding: 16px 6px 14px; }
  .pad-lined .corner { top: 7px; font-size: 6px; }
</style>
</head>
<body>
<svg width="0" height="0" style="position:absolute" aria-hidden="true">
  <symbol id="icon-phone" viewBox="0 0 10 10"><path d="M2 0.5l2 2-1 1.3c.6 1.3 1.6 2.3 2.9 2.9l1.3-1 2 2-1.2 1.8C4.6 9.3.7 5.4.2 1.7z"/></symbol>
  <symbol id="icon-mail" viewBox="0 0 10 10"><path d="M0 2h10v6H0z M0.6 2.4L5 5.6l4.4-3.2" /></symbol>
  <symbol id="icon-web" viewBox="0 0 10 10"><circle cx="5" cy="5" r="4.5"/></symbol>
</svg>

<main class="canvas">

  <!-- Business card, front -->
  <section class="piece card card-front">
    <div class="wordmark on-orange">CRESTWAY</div>
    <div class="tagline light">Coaching and Behavioral Consulting</div>
    <div class="contact">
      218 Larkspur Ave, Suite 210<br>Brookfield, NC 27514<br>
      <svg><use href="#icon-phone"/></svg>(555)214-0873<br>
      <svg><use href="#icon-mail"/></svg>dana@crestway.com<br>
      <svg><use href="#icon-web"/></svg>www.crestway.com
    </div>
    <div class="swoosh" role="img" aria-label="Light diagonal accent field"></div>
    <div class="holder">
      <div class="holder-name">DANA WHITFIELD</div>
      <div class="holder-role">Chief of Staff</div>
    </div>
  </section>

  <!-- Business card, back -->
  <section class="piece card card-back">
    <div class="field" role="img" aria-label="Orange field fading to white"></div>
    <div class="brand">
      <div class="wordmark on-orange">CRESTWAY</div>
      <div class="tagline light">Coaching and Behavioral Consulting</div>
    </div>
  </section>

  <!-- Business envelope, front -->
  <section class="piece envelope-front">
    <div class="wordmark">CRESTWAY</div>
    <div class="tagline">Coaching and Behavioral Consulting</div>
    <div class="contact">218 Larkspur Ave, Suite 210<br>Brookfield, NC 27514</div>
    <div class="faint-band" role="img" aria-label="Faint pale orange accent area"></div>
  </section>

  <!-- Envelope backs -->
  <section class="piece envelope-back envelope-orange">
    <div class="flap"><span class="wordmark on-orange">CRESTWAY</span></div>
  </section>
  <section class="piece envelope-back envelope-dark">
    <div class="flap"><span class="wordmark on-dark">CRESTWAY</span></div>
  </section>

  <!-- Letterhead -->
  <section class="piece letterhead">
    <div class="wordmark">CRESTWAY</div>
    <div class="tagline">Coaching and Behavioral Consulting</div>
    <div class="contact">
      218 Larkspur Ave, Suite 210<br>Brookfield, NC 27514<br>
      <svg><use href="#icon-phone"/></svg>(555)214-0873<br>
      <svg><use href="#icon-mail"/></svg>dana@crestway.com<br>
      <svg><use href="#icon-web"/></svg>www.crestway.com
    </div>
    <div class="faint-band" role="img" aria-label="Faint pale orange accent area"></div>
  </section>

  <!-- Slides -->
  <section class="piece slide slide-1 orange cover">
    <div class="wordmark on-orange">CRESTWAY</div>
    <div class="tagline light">Coaching and Behavioral Consulting</div>
    <h2>Welcome to Our<br>Presentation Name<br>Description</h2>
    <div class="faint-band" role="img" aria-label="White accent field"></div>
  </section>

  <section class="piece slide slide-2">
    <header class="slide-head"><h3>HEADING HERE</h3></header>
    <div class="photo" role="img" aria-label="Photo of colleagues meeting in an office"></div>
    <div class="slide-body">
      <ul>
        <li>Our coaching builds clear goals and steady habits.</li>
        <li>Every plan is shaped around your team.</li>
      </ul>
    </div>
    <div class="slide-foot">WWW.CRESTWAY.COM</div>
  </section>

  <section class="piece slide slide-3">
    <header class="slide-head"><h3>HEADING HERE</h3></header>
    <p class="slide-body" style="margin-top:2px">We partner with leaders to grow trust, focus and lasting change.</p>
    <div class="team">
      <div class="team-member"><div class="portrait" role="img" aria-label="Team member portrait"></div><div class="name">Team member1</div><div class="bio">Title<br>Short bio here.</div></div>
      <div class="team-member"><div class="portrait" role="img" aria-label="Team member portrait"></div><div class="name">Team member2</div><div class="bio">Title<br>Short bio here.</div></div>
      <div class="team-member"><div class="portrait" role="img" aria-label="Team member portrait"></div><div class="name">Team member3</div><div class="bio">Title<br>Short bio here.</div></div>
      <div class="team-member"><div class="portrait" role="img" aria-label="Team member portrait"></div><div class="name">Team member4</div><div class="bio">Title<br>Short bio here.</div></div>
    </div>
    <div class="slide-foot">WWW.CRESTWAY.COM</div>
  </section>

  <section class="piece slide slide-4">
    <header class="slide-head"><h3>HEADING HERE</h3></header>
    <div class="slide-body">
      <ul>
        <li>Set clear targets for each quarter.</li>
        <li>Review progress with your coach.</li>
        <li>Share feedback across every team.</li>
        <li>Celebrate wins and learn from setbacks.</li>
      </ul>
    </div>
    <div class="slide-foot">WWW.CRESTWAY.COM</div>
  </section>

  <section class="piece slide slide-5">
    <header class="slide-head"><h3>HEADING HERE</h3></header>
    <div class="split">
      <div class="text">
        <p class="lead">Steady growth starts with honest reflection</p>
        <p class="slide-body">Each session pairs practical tools with thoughtful questions to move your team forward.</p>
      </div>
      <div class="photo" role="img" aria-label="Photo of glass office towers"></div>
    </div>
    <div class="slide-foot">WWW.CRESTWAY.COM</div>
  </section>

  <section class="piece slide slide-6 orange thanks">
    <div class="faint-band" role="img" aria-label="Soft light accent area"></div>
    <h2>THANKS</h2>
    <div class="meta">
      <div>(555)214-0873<br>dana@crestway.com<br>www.crestway.com</div>
      <div class="right">218 Larkspur Ave<br>Suite 210<br>Brookfield, NC 27514</div>
    </div>
  </section>

  <!-- Rack cards -->
  <section class="piece rack-orange">
    <div class="wordmark on-orange">CRESTWAY</div>
    <div class="tagline light" style="font-size:1.8px">Coaching and Behavioral Consulting</div>
    <div class="contact">(555)214-0873<br>dana@crestway.com<br>www.crestway.com<br>218 Larkspur Ave, Suite 210<br>Brookfield, NC 27514</div>
  </section>
  <section class="piece rack-white">
    <div class="wordmark">CRESTWAY</div>
    <div class="tagline" style="font-size:1.8px">Coaching and Behavioral Consulting</div>
    <div class="base">WWW.CRESTWAY.COM</div>
  </section>

  <!-- Notepads -->
  <section class="piece note-slim lined">
    <span class="corner wordmark">CRESTWAY</span>
    <div class="site">www.crestway.com</div>
  </section>
  <section class="piece pad-orange">
    <div class="spiral"></div>
    <div class="wordmark on-orange">CRESTWAY</div>
    <div class="tagline light">Coaching and Behavioral Consulting</div>
  </section>
  <section class="piece pad-white">
    <div class="spiral"></div>
    <div class="wordmark">CRESTWAY</div>
    <div class="tagline">Coaching and Behavioral Consulting</div>
    <div class="base">WWW.CRESTWAY.COM</div>
  </section>
  <section class="piece pad-lined lined">
    <div class="spiral"></div>
    <span class="corner wordmark">CRESTWAY</span>
    <div class="site" style="font-size:3.4px">www.crestway.com</div>
  </section>

</main>
</body>
</html>
```